Healthcare marketing Website design

This is for a healthcare marketing agency
All details and brief included in the files

I need the design to be incredible!

5 pages to be designed
Home page
About
Portfolio Page
Services
Start your project page

If you need more stock images - download preview images from kestrine pix so I can purchase at a later date

```html
<!DOCTYPE html>
<html lang="en">
<head>
<meta charset="utf-8">
<title>Northlane Consulting — Healthcare Marketing Website</title>
<link href="https://fonts.googleapis.com/css2?family=Quicksand:wght@400;500;600;700&display=swap" rel="stylesheet">
<style>
:root{
  --board-blue:#3f6cd5;
  --board-grey:#eeeef1;
  --cyan:#1aa6ea;
  --navy:#2d4470;
  --ink:#1f2b48;
  --btn-dark:#27375c;
  --footer:#4b4b4f;
  --paper:#ffffff;
  --line:#c9d6e6;
  --frame:#5a5d66;
}
*{box-sizing:border-box}
html,body{margin:0;padding:0}
body{width:1200px;height:3903px;overflow:hidden;position:relative;background:var(--board-grey);font-family:"Quicksand",sans-serif;color:var(--ink)}
.board-blue{position:absolute;left:0;top:0;width:1200px;height:1891px;background:var(--board-blue)}
.screen{position:absolute;overflow:hidden;background:var(--paper)}
.abs{position:absolute}
p{margin:0}
ul{list-style:none;margin:0;padding:0}

.brand{position:absolute;display:flex;align-items:center;gap:5px;color:var(--cyan);font-weight:600;letter-spacing:.01em;line-height:1}
.brand-dot{width:.62em;height:.62em;border-radius:50%;background:var(--navy);flex:none}
.brand.light{color:#fff}
.brand.light .brand-dot{background:#fff}
.btn{position:absolute;display:flex;align-items:center;justify-content:center;border-radius:20px;font-weight:600;text-transform:uppercase;letter-spacing:.03em;white-space:nowrap}
.btn.dark{background:var(--btn-dark);color:#fff}
.btn.outline{border:1.5px solid var(--btn-dark);color:var(--btn-dark)}
.btn.outline-light{border:1.5px solid #fff;color:#fff}
.btn.cyan{background:var(--cyan);color:#fff}
.menu-dots{position:absolute}
.scroll-tag{position:absolute;writing-mode:vertical-rl;font-size:8px;font-weight:600;letter-spacing:.12em;display:flex;align-items:center;gap:6px}
.scroll-tag i{display:block;width:1px;height:34px;background:currentColor}
.glow{position:absolute;border-radius:50%;background:radial-gradient(circle,rgba(60,170,240,.35) 0%,rgba(60,170,240,.12) 45%,rgba(60,170,240,0) 70%)}
.photo{position:absolute}
.photo-doctor{background:linear-gradient(140deg,#2fbaf5 0%,#7cc6ee 35%,#eef2f6 60%,#aebccb 100%)}
.photo-portrait{background:linear-gradient(170deg,#f4f6f9,#c3cfdc)}

/* hero */
.hero{position:relative;width:860px;height:535px;background:var(--paper);overflow:hidden}
.hero h1{position:absolute;left:62px;top:108px;width:345px;margin:0;font-size:20.5px;font-weight:500;line-height:1.38;color:var(--ink)}
.hero .lede{position:absolute;left:62px;top:212px;width:330px;font-size:14.5px;font-weight:500;line-height:1.4}
.stats{position:absolute;left:62px;top:280px;display:flex;gap:13px}
.stat{width:99px;height:85px;border:1.5px solid var(--line);border-radius:9px;padding:9px 10px}
.stat b{display:block;color:var(--cyan);font-size:15px;font-weight:600;margin-bottom:4px}
.stat span{display:block;font-size:7px;line-height:1.35;color:#3a4256}

/* helping */
.helping{position:relative;width:860px;height:536px;background:var(--navy);overflow:hidden}
.helping .band{position:absolute;left:0;top:0;width:860px;height:110px;background:var(--cyan)}
.helping h2{position:absolute;left:62px;top:168px;margin:0;font-size:36px;font-weight:500;line-height:1.45;color:#fff;letter-spacing:.01em}
.helping h2 span{color:var(--cyan)}
.helping .copy{position:absolute;left:62px;top:298px;width:365px;color:#e8eef8;font-size:8.6px;line-height:1.65}
.helping .copy p+p{margin-top:12px}
.helping .figures{position:absolute;left:585px;top:358px;width:232px;color:#fff;font-size:11.5px}
.helping .figures li{padding:9px 0 9px;border-bottom:1px solid rgba(255,255,255,.45)}
.helping .figures li:last-child{border-bottom:0}

/* footer */
.site-footer{position:relative;width:638px;height:147px;background:var(--footer);color:#eee;font-size:7px}
.site-footer .signup-title{position:absolute;left:39px;top:37px}
.site-footer .field{position:absolute;left:39px;width:120px;border-bottom:1px solid rgba(255,255,255,.6);padding-bottom:3px;font-size:6.5px}
.site-footer .send{position:absolute;left:39px;top:98px;width:47px;height:13px;border:1px solid rgba(255,255,255,.8);border-radius:8px;font-size:6px;display:flex;align-items:center;justify-content:center}
.site-footer .links{position:absolute;top:33px;line-height:10.6px}
.site-footer .contact{position:absolute;right:46px;top:37px;text-align:right}
.site-footer .social{display:flex;gap:7px;justify-content:flex-end;margin:9px 0 9px}
.site-footer .social span{width:9px;height:9px;border-radius:50%;background:#fff}

/* about */
.about .label{position:absolute;left:39px;top:91px;font-size:11px;font-weight:600}
.about .intro{position:absolute;left:39px;top:133px;width:370px;font-size:15px;font-weight:500;line-height:1.36}
.person{position:absolute;width:125px}
.person .photo{position:relative;width:125px;height:121px}
.person b{display:block;margin-top:10px;font-size:8.5px;color:var(--cyan);font-weight:600}
.person small{display:block;margin-top:4px;font-size:6.2px;color:#222;font-weight:600}

/* services */
.service .label{position:absolute;left:39px;top:66px;font-size:8px;font-weight:600}
.service .intro{position:absolute;left:39px;top:86px;width:262px;font-size:5.8px;line-height:1.55;color:#3c4660}
.service .intro p+p{margin-top:7px}
.service .list{position:absolute;left:0;top:277px;width:477px;height:501px;background:var(--navy)}
.offer{position:absolute;left:47px;width:400px;color:#fff}
.offer h3{margin:0;font-size:16px;font-weight:500;line-height:1.4;width:120px}
.offer h3 sup{font-size:5px;color:var(--cyan);margin-right:3px;vertical-align:top;position:relative;top:2px}
.offer p{position:absolute;left:209px;top:0;width:185px;font-size:4.8px;line-height:1.5;color:#dfe6f2}
.offer-rule{position:absolute;left:39px;width:400px;height:1px;background:rgba(255,255,255,.18)}
.service .cta{position:absolute;left:0;top:778px;width:477px;height:100px;background:var(--cyan)}

/* home */
.mission{position:absolute;left:0;top:341px;width:539px;height:292px;background:var(--cyan);color:#fff;text-align:center}
.mission h3{position:absolute;left:40px;top:80px;width:459px;margin:0;font-size:12px;font-weight:500}
.mission p{position:absolute;left:76px;top:106px;width:388px;font-size:8.4px;line-height:1.62}
.quotes{position:absolute;left:0;top:969px;width:539px;height:154px;background:var(--cyan);color:#fff}
.faq{position:absolute;left:0;top:1123px;width:539px;height:260px;background:var(--navy);color:#fff}
.faq h3{position:absolute;left:37px;top:37px;margin:0;font-size:17.5px;font-weight:500}
.faq-row{position:absolute;left:39px;width:461px;border-bottom:1px solid rgba(255,255,255,.5);padding-bottom:9px;font-size:8.5px;font-weight:500}
.plus{position:absolute;right:0;top:-2px;width:14px;height:14px;border:1px solid #fff;border-radius:50%}
.plus::before,.plus::after{content:"";position:absolute;left:3px;top:6px;width:6px;height:1px;background:#fff}
.plus::after{transform:rotate(90deg)}
.blog h3{position:absolute;left:37px;top:1425px;margin:0;font-size:17.5px;font-weight:500;color:var(--ink)}
.post{position:absolute;top:1469px;width:129px}
.post .photo{position:relative;width:129px;height:76px}
.post b{display:block;margin-top:10px;font-size:6.8px;line-height:1.35;font-weight:700}
.post span{display:block;margin-top:5px;font-size:5px;line-height:1.45;color:#555}
.arrow-ring{position:absolute;width:16px;height:16px;border:1px solid currentColor;border-radius:50%}
.arrow-ring::after{content:"";position:absolute;left:4px;top:5px;width:4px;height:4px;border-top:1px solid currentColor;border-right:1px solid currentColor;transform:rotate(45deg)}

/* portfolio */
.portfolio{border:3px solid var(--frame);border-right:0;box-shadow:0 4px 14px rgba(0,0,0,.12)}
.portfolio .label{position:absolute;left:32px;top:97px;font-size:10.5px;font-weight:600}
.portfolio .headline{position:absolute;left:32px;top:126px;font-size:14px;font-weight:500}
.portfolio .headline span{color:var(--cyan)}
.portfolio .sub{position:absolute;left:32px;top:158px;width:350px;font-size:14px;font-weight:500;line-height:1.45}
.project-name{position:absolute;font-size:9px;font-weight:600}

/* menu */
.menu-screen{box-shadow:0 4px 14px rgba(0,0,0,.14)}
.menu-shade{position:absolute;left:0;top:0;width:541px;height:330px;background:rgba(120,122,128,.45)}
.menu-panel{position:absolute;left:283px;top:0;width:258px;height:330px;background:var(--navy);color:#fff}
.menu-panel ul{position:absolute;right:40px;top:46px;text-align:right;font-size:13px;font-weight:500;line-height:31.5px}
.menu-panel .social{position:absolute;right:40px;top:266px;display:flex;gap:10px}
.menu-panel .social span{width:12px;height:12px;border-radius:50%;background:#fff}
</style>
</head>
<body>
<div class="board-blue"></div>

<!-- home hero screen -->
<div class="screen" style="left:52px;top:109px;width:866px;height:541px;border:3px solid var(--frame)">
  <section class="hero">
    <div class="glow" style="left:-90px;top:50px;width:260px;height:260px"></div>
    <div class="brand" style="left:64px;top:21px;font-size:17px"><span class="brand-dot"></span>northlane</div>
    <span class="btn dark" style="left:643px;top:18px;width:133px;height:21px;font-size:8px">Start your project</span>
    <svg class="menu-dots" style="left:783px;top:20px" width="18" height="18" viewBox="0 0 18 18"><g fill="#27375c"><circle cx="3" cy="3" r="2"/><circle cx="9" cy="3" r="2"/><circle cx="15" cy="3" r="2"/><circle cx="3" cy="9" r="2"/><circle cx="9" cy="9" r="2"/><circle cx="15" cy="9" r="2"/><circle cx="3" cy="15" r="2"/><circle cx="9" cy="15" r="2"/><circle cx="15" cy="15" r="2"/></g></svg>
    <h1>Don’t miss a new opportunity to grow you practice with your online presence</h1>
    <p class="lede">Being online: a large opportunity for your practice</p>
    <div class="stats">
      <div class="stat"><b>80%</b><span>of internet users search for health information</span></div>
      <div class="stat"><b>50%</b><span>would like information about a specific health professionals</span></div>
      <div class="stat"><b>42%</b><span>of individuals look at health related consumer reviews</span></div>
      <div class="stat"><b>41%</b><span>of consumers say online presence may impact their choice of health professional</span></div>
    </div>
    <span class="btn outline" style="left:62px;top:394px;width:109px;height:29px;font-size:8px">Contact us</span>
    <span class="btn dark" style="left:188px;top:394px;width:136px;height:29px;font-size:8px">Start your project</span>
    <div class="photo photo-doctor" role="img" aria-label="Doctor in a white coat with a stethoscope holding a tablet" style="left:500px;top:90px;width:290px;height:330px"></div>
    <div class="scroll-tag" style="left:812px;top:300px;color:#27375c">01<i></i>SCROLL</div>
  </section>
</div>

<!-- helping screen -->
<div class="screen" style="left:306px;top:679px;width:866px;height:542px;border:3px solid var(--frame)">
  <section class="helping">
    <div class="band"></div>
    <div class="brand light" style="left:30px;top:40px;font-size:24px"><span class="brand-dot"></span>northlane</div>
    <div class="photo photo-portrait" role="img" aria-label="Portrait of a smiling man wearing glasses" style="left:520px;top:30px;width:290px;height:290px"></div>
    <h2>Helping Clients<br><span>Since 2015</span></h2>
    <div class="copy">
      <p><b>Northlane Consulting</b> specialises in helping health professionals like you, stand out from the busy crowd, find new patient and helps you be seen as the go-to person within your industry. Unlike most health professionals who solely rely on word of mouth, we use the latest online marketing techniques to grow you and your practice.</p>
      <p>While our niche has always been in the healthcare industry, Northlane Marketing also has experience in providing solutions our e-commerce partners as well as other professional industries.</p>
    </div>
    <span class="btn outline-light" style="left:62px;top:448px;width:109px;height:27px;font-size:8px">Contact us</span>
    <span class="btn cyan" style="left:188px;top:448px;width:136px;height:27px;font-size:8px">Start your project</span>
    <ul class="figures"><li>63% Healthcare and medical</li><li>25% Ecommerce projects</li><li>12% Other professional services</li></ul>
    <div class="scroll-tag" style="left:835px;top:268px;color:#fff">03<i></i>SCROLL</div>
  </section>
</div>

<!-- about screen -->
<div class="screen about" style="left:0;top:1259px;width:638px;height:782px">
  <div class="brand" style="left:39px;top:14px;font-size:13px"><span class="brand-dot"></span>northlane</div>
  <span class="btn dark" style="left:474px;top:11px;width:90px;height:16px;font-size:6px">Start your project</span>
  <svg class="menu-dots" style="left:578px;top:12px" width="13" height="13" viewBox="0 0 18 18"><g fill="#27375c"><circle cx="3" cy="3" r="2"/><circle cx="9" cy="3" r="2"/><circle cx="15" cy="3" r="2"/><circle cx="3" cy="9" r="2"/><circle cx="9" cy="9" r="2"/><circle cx="15" cy="9" r="2"/><circle cx="3" cy="15" r="2"/><circle cx="9" cy="15" r="2"/><circle cx="15" cy="15" r="2"/></g></svg>
  <p class="label">About Us</p>
  <p class="intro">We specialise in providing website and online marketing services to business owners who are looking to find new customers through online marketing. While we do service all types of businesses, our niche has always been the healthcare and medical field.</p>
  <div class="glow" style="left:120px;top:320px;width:260px;height:260px"></div>
  <div class="glow" style="left:330px;top:300px;width:260px;height:260px"></div>
  <div class="person" style="left:39px;top:326px"><div class="photo" role="img" aria-label="Black and white portrait of team member" style="background:linear-gradient(160deg,#e6e6e6,#8c8c8c)"></div><b>Person 1</b><small>Northlane Marketing Founder</small></div>
  <div class="person" style="left:177px;top:371px"><div class="photo" role="img" aria-label="Black and white portrait of team member" style="background:linear-gradient(160deg,#dedede,#7d7d7d)"></div><b>Person 2</b><small>Creative Content Manager</small></div>
  <div class="person" style="left:317px;top:326px"><div class="photo" role="img" aria-label="Black and white portrait of team member" style="background:linear-gradient(160deg,#e2e2e2,#5f5f5f)"></div><b>Person 3</b><small>Operations and Service Manager</small></div>
  <div class="person" style="left:468px;top:386px"><div class="photo" role="img" aria-label="Black and white portrait of team member" style="background:linear-gradient(160deg,#e4e4e4,#6a6a6a)"></div><b>Person 4</b><small>Junior Website Developer</small></div>
  <div class="abs" style="left:0;top:635px">
    <footer class="site-footer">
      <p class="signup-title">Sign up to our mailing list</p>
      <div class="field" style="top:54px">Name</div>
      <div class="field" style="top:76px">Email</div>
      <span class="send">SEND</span>
      <ul class="links" style="left:235px"><li>Home</li><li>About</li><li>Portfolio</li><li>Contact Us</li><li>Our Services</li><li>Blog</li></ul>
      <ul class="links" style="left:347px"><li>Privacy Policy</li><li>Terms and Conditions</li></ul>
      <div class="contact">info@northlaneconsulting.example<div class="social"><span></span><span></span></div>All rights reserved 2022</div>
    </footer>
  </div>
</div>

<!-- services screen -->
<div class="screen service" style="left:723px;top:1359px;width:477px;height:986px">
  <div class="brand" style="left:39px;top:10px;font-size:11px"><span class="brand-dot"></span>northlane</div>
  <span class="btn dark" style="left:357px;top:8px;width:68px;height:12px;font-size:4.6px">Start your project</span>
  <svg class="menu-dots" style="left:430px;top:8px" width="11" height="11" viewBox="0 0 18 18"><g fill="#27375c"><circle cx="3" cy="3" r="2"/><circle cx="9" cy="3" r="2"/><circle cx="15" cy="3" r="2"/><circle cx="3" cy="9" r="2"/><circle cx="9" cy="9" r="2"/><circle cx="15" cy="9" r="2"/><circle cx="3" cy="15" r="2"/><circle cx="9" cy="15" r="2"/><circle cx="15" cy="15" r="2"/></g></svg>
  <p class="label">Our Service</p>
  <div class="intro">
    <p>You became a business owner because you wanted to make a difference. At first things were great and customers were plentiful. In the last few years there's more competition offering the same types of services and products as you do. Regular customers haven't come back to your business in a while and you know you NEED to do something but the old ways like relying on word of mouth doesn't seem to be working well anymore and you don't know how to get started.</p>
    <p>But that's where we can help. Northlane Consulting helps business owners like you to build your online presence through website design and development, social media management and online traffic strategies. While we do service all types of businesses, our specialty has always been the healthcare and medical field.</p>
  </div>
  <div class="glow" style="left:250px;top:20px;width:250px;height:250px"></div>
  <div class="photo" role="img" aria-label="Businesswoman working on a laptop" style="left:318px;top:46px;width:130px;height:204px;background:linear-gradient(170deg,#f1f4f7,#9aa9b8)"></div>
  <div class="list">
    <div class="offer" style="top:38px"><h3><sup>01</sup>Website Development</h3><p>Your website is your most valuable digital asset. It works for you around the clock, so we build fast, clear and trusted sites that turn visitors into new patients and keep them coming back to your practice.</p></div>
    <div class="offer-rule" style="top:120px"></div>
    <div class="offer" style="top:150px"><h3><sup>02</sup>Customer Acquisition</h3><p>Business owners like you need to be more focused on reaching the right people. We plan campaigns that find new clients for your practice and take the time to understand your business needs.</p></div>
    <div class="offer-rule" style="top:223px"></div>
    <div class="offer" style="top:253px"><h3><sup>03</sup>Social Media Management</h3><p>Posting often on social media is not the best way to get noticed. We create meaningful and engaging content through strategy, so your audience knows you and chooses you over your competition.</p></div>
    <div class="offer-rule" style="top:332px"></div>
    <div class="offer" style="top:364px"><h3><sup>04</sup>Online Traffic Strategies</h3><p>There are more customers searching for information online than ever. Our tailored search and email strategies bring more relevant traffic to your website and help grow your online reach.</p></div>
    <div class="abs" style="left:182px;top:452px;color:#fff;font-size:7px;display:flex;align-items:center;gap:6px">View our portfolio <span class="arrow-ring" style="position:relative;width:13px;height:13px"></span></div>
  </div>
  <div class="cta">
    <p class="abs" style="left:37px;top:22px;width:230px;color:#fff;font-size:15.5px;font-weight:500;line-height:1.45">Let’s start something completely new together</p>
    <span class="btn outline-light" style="left:289px;top:41px;width:58px;height:13px;font-size:4.6px;border-width:1px">Contact us</span>
    <span class="btn" style="left:357px;top:41px;width:76px;height:13px;font-size:4.6px;background:var(--btn-dark);color:#fff">Start your project</span>
  </div>
  <div class="abs" style="left:0;top:878px;width:638px;transform:scale(.7476);transform-origin:0 0">
    <footer class="site-footer">
      <p class="signup-title">Sign up to our mailing list</p>
      <div class="field" style="top:54px">Name</div>
      <div class="field" style="top:76px">Email</div>
      <span class="send">SEND</span>
      <ul class="links" style="left:235px"><li>Home</li><li>About</li><li>Portfolio</li><li>Contact Us</li><li>Our Services</li><li>Blog</li></ul>
      <ul class="links" style="left:347px"><li>Privacy Policy</li><li>Terms and Conditions</li></ul>
      <div class="contact">info@northlaneconsulting.example<div class="social"><span></span><span></span></div>All rights reserved 2022</div>
    </footer>
  </div>
</div>

<!-- full home page screen -->
<div class="screen home" style="left:61px;top:2079px;width:539px;height:1774px">
  <div class="abs" style="left:0;top:0;transform:scale(.627);transform-origin:0 0">
    <section class="hero">
      <div class="glow" style="left:-90px;top:50px;width:260px;height:260px"></div>
      <div class="brand" style="left:64px;top:21px;font-size:17px"><span class="brand-dot"></span>northlane</div>
      <span class="btn dark" style="left:643px;top:18px;width:133px;height:21px;font-size:8px">Start your project</span>
      <svg class="menu-dots" style="left:783px;top:20px" width="18" height="18" viewBox="0 0 18 18"><g fill="#27375c"><circle cx="3" cy="3" r="2"/><circle cx="9" cy="3" r="2"/><circle cx="15" cy="3" r="2"/><circle cx="3" cy="9" r="2"/><circle cx="9" cy="9" r="2"/><circle cx="15" cy="9" r="2"/><circle cx="3" cy="15" r="2"/><circle cx="9" cy="15" r="2"/><circle cx="15" cy="15" r="2"/></g></svg>
      <h1>Don’t miss a new opportunity to grow you practice with your online presence</h1>
      <p class="lede">Being online: a large opportunity for your practice</p>
      <div class="stats">
        <div class="stat"><b>80%</b><span>of internet users search for health information</span></div>
        <div class="stat"><b>50%</b><span>would like information about a specific health professionals</span></div>
        <div class="stat"><b>42%</b><span>of individuals look at health related consumer reviews</span></div>
        <div class="stat"><b>41%</b><span>of consumers say online presence may impact their choice of health professional</span></div>
      </div>
      <span class="btn outline" style="left:62px;top:394px;width:109px;height:29px;font-size:8px">Contact us</span>
      <span class="btn dark" style="left:188px;top:394px;width:136px;height:29px;font-size:8px">Start your project</span>
      <div class="photo photo-doctor" role="img" aria-label="Doctor in a white coat with a stethoscope holding a tablet" style="left:500px;top:90px;width:290px;height:330px"></div>
      <div class="scroll-tag" style="left:812px;top:300px;color:#27375c">01<i></i>SCROLL</div>
    </section>
  </div>

  <section class="mission">
    <h3>Northlane Consulting: helping those who help others</h3>
    <p>You become a health professional because you wanted to make a difference and you obviously care about patient outcomes. At first things were great and you had plenty of patients but in the last few years there's more competition offering the same types of services and products that you do. Regular customers haven't come back to you in a while and you know you NEED to do something but the old ways like relying on word of mouth doesn't seem to be working well anymore and you don't know how to get started. But that's where we can help. Northlane Consulting specialises in helping health professionals like you to create a great online user experience for your patients</p>
    <div class="scroll-tag" style="left:513px;top:140px;color:#fff">02<i></i>SCROLL</div>
  </section>

  <div class="abs" style="left:0;top:633px;transform:scale(.627);transform-origin:0 0">
    <section class="helping">
      <div class="band"></div>
      <div class="brand light" style="left:30px;top:40px;font-size:24px"><span class="brand-dot"></span>northlane</div>
      <div class="photo photo-portrait" role="img" aria-label="Portrait of a smiling man wearing glasses" style="left:520px;top:30px;width:290px;height:290px"></div>
      <h2>Helping Clients<br><span>Since 2015</span></h2>
      <div class="copy">
        <p><b>Northlane Consulting</b> specialises in helping health professionals like you, stand out from the busy crowd, find new patient and helps you be seen as the go-to person within your industry. Unlike most health professionals who solely rely on word of mouth, we use the latest online marketing techniques to grow you and your practice.</p>
        <p>While our niche has always been in the healthcare industry, Northlane Marketing also has experience in providing solutions our e-commerce partners as well as other professional industries.</p>
      </div>
      <span class="btn outline-light" style="left:62px;top:448px;width:109px;height:27px;font-size:8px">Contact us</span>
      <span class="btn cyan" style="left:188px;top:448px;width:136px;height:27px;font-size:8px">Start your project</span>
      <ul class="figures"><li>63% Healthcare and medical</li><li>25% Ecommerce projects</li><li>12% Other professional services</li></ul>
      <div class="scroll-tag" style="left:835px;top:268px;color:#fff">03<i></i>SCROLL</div>
    </section>
  </div>

  <section class="quotes">
    <p class="abs" style="left:39px;top:58px;width:160px;font-size:17px;font-weight:500;line-height:1.4">See What Our Clients Say</p>
    <p class="abs" style="left:257px;top:48px;font-size:9px;letter-spacing:1px;color:#fff">•••</p>
    <p class="abs" style="left:257px;top:66px;width:215px;font-size:6px;line-height:1.5">Lorem ipsum dolor sit amet, consectetur adipiscing elit, sed do eiusmod tempor incididunt ut labore et dolore magna aliqua. Ut enim ad minim veniam, quis nostrud exercitation ullamco laboris nisi ut aliquip ex ea commodo consequat.</p>
    <p class="abs" style="left:257px;top:106px;font-size:6px;line-height:1.4">John Doe<br><span style="font-size:4.8px">Senior Manager</span></p>
    <span class="arrow-ring" style="left:478px;top:43px;color:#fff"></span>
  </section>

  <section class="faq">
    <h3>Frequently Asked Questions</h3>
    <div class="faq-row" style="top:100px">Lorem ipsum dolor sit amet, consectetur adipiscing elit,<span class="plus"></span></div>
    <div class="faq-row" style="top:136px">How much do your service cost<span class="plus"></span></div>
    <div class="faq-row" style="top:174px">Who will i communicate with?<span class="plus"></span></div>
  </section>

  <section class="blog">
    <h3>Our Last Blog</h3>
    <span class="arrow-ring" style="left:484px;top:1429px;color:var(--ink)"></span>
    <div class="post" style="left:39px"><div class="photo" role="img" aria-label="Two smartphones on an orange backdrop" style="background:linear-gradient(135deg,#f4a236,#d9641a)"></div><b>Lorem ipsum dolor sit amet, consectetur adipiscing elit</b><span>Lorem ipsum dolor sit amet, consectetur adipiscing elit. Lectus placerat eget faucibus tortor ac pharetra arcu. Dictum lectus non et mauris felis sagittis nam.</span></div>
    <div class="post" style="left:204px"><div class="photo" role="img" aria-label="Figure against a warm fire-lit background" style="background:linear-gradient(135deg,#e88a2a,#5a2a10)"></div><b>Lorem ipsum dolor sit amet, consectetur adipiscing elit</b><span>Lorem ipsum dolor sit amet, consectetur adipiscing elit. Lectus placerat eget faucibus tortor ac pharetra arcu. Dictum lectus non et mauris felis sagittis nam.</span></div>
    <div class="post" style="left:370px"><div class="photo" role="img" aria-label="Dark interior scene with blue light" style="background:linear-gradient(135deg,#2d3d5c,#0f1626)"></div><b>Lorem ipsum dolor sit amet, consectetur adipiscing elit</b><span>Lorem ipsum dolor sit amet, consectetur adipiscing elit. Lectus placerat eget faucibus tortor ac pharetra arcu. Dictum lectus non et mauris felis sagittis nam.</span></div>
  </section>

  <div class="abs" style="left:0;top:1648px;width:638px;transform:scale(.845);transform-origin:0 0">
    <footer class="site-footer">
      <p class="signup-title">Sign up to our mailing list</p>
      <div class="field" style="top:54px">Name</div>
      <div class="field" style="top:76px">Email</div>
      <span class="send">SEND</span>
      <ul class="links" style="left:235px"><li>Home</li><li>About</li><li>Portfolio</li><li>Contact Us</li><li>Our Services</li><li>Blog</li></ul>
      <ul class="links" style="left:347px"><li>Privacy Policy</li><li>Terms and Conditions</li></ul>
      <div class="contact">info@northlaneconsulting.example<div class="social"><span></span><span></span></div>All rights reserved 2022</div>
    </footer>
  </div>
</div>

<!-- portfolio screen -->
<div class="screen portfolio" style="left:641px;top:2454px;width:559px;height:538px">
  <div class="brand" style="left:32px;top:22px;font-size:13px"><span class="brand-dot"></span>northlane</div>
  <span class="btn dark" style="left:480px;top:15px;width:110px;height:16px;font-size:6px">Start your project</span>
  <div class="glow" style="left:380px;top:60px;width:240px;height:240px"></div>
  <p class="label">Portfolio</p>
  <p class="headline">Every online marketing <span>project is unique</span></p>
  <p class="sub">Here are some of our latest projects that we were lucky to work on</p>
  <div class="photo" role="img" aria-label="Optical store website shown on a laptop mockup" style="left:32px;top:260px;width:248px;height:185px;background:linear-gradient(150deg,#d5e0ea,#a9bccd)"></div>
  <p class="project-name" style="left:32px;top:457px">Harlow Optics</p>
  <div class="photo" role="img" aria-label="Windscreen repair website with a service van" style="left:356px;top:294px;width:210px;height:182px;background:linear-gradient(160deg,#f2f2f2 0%,#e9e9ea 55%,#c8ccd2 100%)"></div>
  <p class="project-name" style="left:356px;top:494px">Citywide Screen Repair</p>
</div>

<!-- menu screen -->
<div class="screen menu-screen" style="left:645px;top:3068px;width:541px;height:330px">
  <div class="abs" style="left:0;top:0;transform:scale(.627);transform-origin:0 0">
    <section class="hero">
      <div class="glow" style="left:-90px;top:50px;width:260px;height:260px"></div>
      <div class="brand" style="left:64px;top:21px;font-size:17px"><span class="brand-dot"></span>northlane</div>
      <h1>Don’t miss a new opportunity to grow you practice with your online presence</h1>
      <p class="lede">Being online: a large opportunity for your practice</p>
      <div class="stats">
        <div class="stat"><b>80%</b><span>of internet users search for health information</span></div>
        <div class="stat"><b>50%</b><span>would like information about a specific health professionals</span></div>
        <div class="stat"><b>42%</b><span>of individuals look at health related consumer reviews</span></div>
        <div class="stat"><b>41%</b><span>of consumers say online presence may impact their choice of health professional</span></div>
      </div>
      <span class="btn outline" style="left:62px;top:394px;width:109px;height:29px;font-size:8px">Contact us</span>
      <span class="btn dark" style="left:188px;top:394px;width:136px;height:29px;font-size:8px">Start your project</span>
    </section>
  </div>
  <div class="menu-shade"></div>
  <nav class="menu-panel">
    <ul><li>Home</li><li>About</li><li>Portfolio</li><li>Our Services</li><li>Blog</li><li>Contact Us</li></ul>
    <div class="social"><span></span><span></span></div>
  </nav>
</div>
</body>
</html>
```